Popup-Fenster Design für Öffnungszeiten
Zielgruppe
Planung und Realisierung von individuellen Kaminen.
Aufgabenstellung
Für unsere Website www.lindenhaus-torvel.de benötigen wir ein Popup-Fenster für die Startseite. Da das Geschäft nicht jeden Tag und zu festen Zeit geöffnet hat, soll der Kunde direkt sehen können, wann das Geschäft das nächste Mal geöffnet hat. Das Popup-Fenster soll auffällig, jedoch nicht überladen und aufdringlich sein. Einen eigenen Entwurf (der mir nicht gefällt) habe ich hochgeladen. Vielleicht benötigt dieser nur noch einen Feinschliff!? Es muss nicht reckteckig sein, ich bin auch für runde oder ovale Formen offen. Der dort eingesetzte Text sollte als Platzhalter eingesetzt werden. Bei Fragen können Sie mir gerne eine Nachricht zukommen lassen.

```html
<!DOCTYPE html>
<html lang="de">
<head>
<meta charset="utf-8">
<title>Lindenhaus – Öffnungszeiten</title>
<link rel="stylesheet" href="https://fonts.googleapis.com/css2?family=Raleway:wght@200;300;400&family=Playfair+Display:ital,wght@1,700&family=Dancing+Script:wght@700&family=Tinos&display=swap">
<style>
  :root {
    --sidebar-bg: #1b1b1b;
    --nav-text: #8d8882;
    --brand-gold: #b59a4f;
    --white: #ffffff;
    --popup-top: #505053;
    --popup-bottom: #121212;
    --popup-band: #000000;
    --popup-muted: #c4c4c4;
    --divider: #6a6a6a;
    --hero-sky: #c9d2dc;
    --hero-mid: #7d7a70;
    --hero-ground: #a8a195;
  }
  * { margin: 0; padding: 0; box-sizing: border-box; }
  html, body { width: 1200px; height: 577px; overflow: hidden; background: var(--sidebar-bg); }
  .page { position: relative; width: 1200px; height: 577px; }

  .sidebar {
    position: absolute; left: 0; top: 0; width: 263px; height: 577px;
    background: var(--sidebar-bg);
    font-family: "Raleway", sans-serif;
  }
  .brand {
    position: absolute; top: 58px; left: 0; width: 263px;
    display: flex; flex-direction: column; align-items: center; gap: 14px;
  }
  .brand-square { width: 44px; height: 44px; background: var(--brand-gold); }
  .brand-name {
    color: var(--brand-gold); font-size: 13px; font-weight: 400; letter-spacing: 3px;
  }
  .nav { position: absolute; left: 44px; top: 224px; list-style: none; }
  .nav li {
    color: var(--nav-text); font-size: 16px; font-weight: 300;
    height: 45.6px; line-height: 20px;
  }
  .legal {
    position: absolute; left: 44px; top: 538px;
    color: var(--nav-text); font-size: 11px; font-weight: 300;
  }

  .hero {
    position: absolute; left: 263px; top: 0; width: 937px; height: 577px;
    background: linear-gradient(180deg, var(--hero-sky) 0%, #9fb0c2 22%, #6b6d6b 36%, var(--hero-mid) 55%, var(--hero-ground) 80%, #b89a7a 100%);
  }
  .hero-title {
    position: absolute; left: 263px; width: 937px; top: 224px; text-align: center;
    color: var(--white); font-family: "Raleway", sans-serif; font-weight: 200;
    font-size: 51px; letter-spacing: 0.5px;
  }
  .hero-tagline {
    position: absolute; left: 263px; width: 937px; top: 285px; text-align: center;
    color: var(--white); font-family: "Playfair Display", serif; font-style: italic;
    font-weight: 700; font-size: 32px;
  }
  .hero-cta {
    position: absolute; left: 619px; top: 509px;
    color: #3a3a3a; font-family: "Raleway", sans-serif; font-size: 11px; letter-spacing: 2px;
  }
  .hero-chevron { position: absolute; left: 725px; top: 535px; }

  .hours-popup {
    position: absolute; left: 752px; top: 324px; width: 425px; height: 236px;
    background: linear-gradient(180deg, var(--popup-top) 0%, #303032 45%, var(--popup-bottom) 100%);
    border-radius: 0 0 14px 14px;
    box-shadow: 0 4px 12px rgba(0,0,0,0.4);
    font-family: "Tinos", serif; color: var(--white); text-align: center;
  }
  .hours-band {
    position: absolute; left: 0; top: 18px; width: 425px; height: 45px;
    background: var(--popup-band); border-bottom: 2px solid #8a8a8a;
  }
  .hours-title {
    font-family: "Dancing Script", cursive; font-weight: 700; font-size: 40px;
    line-height: 48px; margin-top: -2px;
  }
  .hours-lead { position: absolute; top: 86px; width: 100%; font-size: 18px; letter-spacing: 0.3px; }
  .hours-list { position: absolute; top: 118px; width: 100%; font-size: 16px; line-height: 20px; }
  .hours-list span { display: inline-block; }
  .hours-list .day { width: 82px; text-align: left; }
  .hours-list .time { width: 130px; text-align: left; }
  .hours-divider {
    position: absolute; top: 172px; left: 41px; width: 342px; height: 1px; background: var(--divider);
  }
  .hours-more { position: absolute; top: 181px; width: 100%; font-size: 15px; line-height: 21px; color: var(--popup-muted); }

  .popup-close {
    position: absolute; left: 1160px; top: 310px; width: 30px; height: 30px; border-radius: 50%;
    background: #000; border: 1px solid #444; color: var(--white);
    font-family: "Raleway", sans-serif; font-weight: 400; font-size: 16px;
    display: flex; align-items: center; justify-content: center;
  }
</style>
</head>
<body>
<div class="page">
  <aside class="sidebar">
    <div class="brand">
      <div class="brand-square"></div>
      <div class="brand-name">LINDENHAUS</div>
    </div>
    <ul class="nav">
      <li>ÜBER UNS</li>
      <li>KAMINÖFEN</li>
      <li>HOLZKAMINE</li>
      <li>GASKAMINE</li>
      <li>AUSSTELLUNG</li>
      <li>KONTAKT</li>
    </ul>
    <div class="legal">Impressum | Datenschutz</div>
  </aside>

  <div class="hero" role="img" aria-label="Hängender schwarzer Designkamin vor einer Glasfront mit Blick auf eine verschneite Berglandschaft"></div>
  <h1 class="hero-title">WILLKOMMEN IM LINDENHAUS</h1>
  <p class="hero-tagline">KAMINE FÜRS LEBEN</p>
  <p class="hero-cta">Jetzt Beratungstermin</p>
  <svg class="hero-chevron" width="14" height="8" viewBox="0 0 14 8"><polyline points="1,1 7,7 13,1" fill="none" stroke="#3a3a3a" stroke-width="1.4"/></svg>

  <section class="hours-popup">
    <div class="hours-band"><h2 class="hours-title">Öffnungszeiten</h2></div>
    <p class="hours-lead">WIR HABEN FÜR SIE GEÖFFNET:</p>
    <div class="hours-list">
      <div><span class="day">Fr&nbsp; 17.01</span><span class="time">14:00 - 17:00 Uhr</span></div>
      <div><span class="day">Sa&nbsp; 18.01</span><span class="time">10:00 - 13:00 Uhr</span></div>
    </div>
    <div class="hours-divider"></div>
    <p class="hours-more">Weitere Termine ansehen Indiviudellen<br>Termin vereinbaren</p>
  </section>
  <div class="popup-close">X</div>
</div>
</body>
</html>
```